Indian Takeaway Menu -

I would like to have double parallel fold A4 sheet menu.
A4 sheet cut in half and attached to the other half to make the sheet 4 small pages long.

Colors
abd036
ffffff

Requirements
Must have
• Please check new attachments - menu size and layout is not correct.
• I would like to add Dark brown colour. A4 sheet folded 4x Menu layout pocket size.
Nice to have
• Dark Brown - Parrot Green and very light Brown

```html
<!DOCTYPE html>
<html lang="en">
<head>
<meta charset="utf-8">
<title>Saffron Lane – Takeaway Menu Layout</title>
<link href="https://fonts.googleapis.com/css2?family=Open+Sans:ital,wght@0,400;0,600;0,700;0,800;1,400;1,600;1,700;1,800&display=swap" rel="stylesheet">
<style>
:root{
  --green:#abd036;
  --white:#ffffff;
  --stage:#d9d9d9;
  --ink:#1d1d1d;
  --muted:#333;
  --label:#2a2a2a;
}
*{box-sizing:border-box;margin:0;padding:0}
html,body{width:1200px;height:1200px;overflow:hidden}
body{background:var(--stage);font-family:"Open Sans",Arial,sans-serif;color:var(--ink);position:relative}
.side-label{position:absolute;font-size:31px;font-weight:400;color:var(--label);letter-spacing:.5px}
.sheet{position:absolute;display:flex;background:var(--white);box-shadow:6px 8px 14px rgba(0,0,0,.35)}
.panel{width:50%;height:100%;position:relative;display:flex;flex-direction:column;padding:14px 12px}
.panel.green{background:var(--green)}
.panel.white{background:var(--white)}
.item{margin-bottom:7px}
.item .name{display:flex;align-items:baseline;font-style:italic;font-weight:700;font-size:7px;line-height:1.2}
.item .name .dots{flex:1;border-bottom:1px dotted var(--ink);margin:0 2px;transform:translateY(-2px)}
.item .desc{font-size:5.8px;line-height:1.25;color:var(--muted)}
.item ul{list-style:none;font-size:5.8px;line-height:1.3;color:var(--muted)}
.head-box{border:1.5px solid var(--white);color:var(--white);text-align:center;font-style:italic;font-weight:700;font-size:11.5px;padding:2px 0;margin:4px 6px 10px}
.head-bar{background:var(--green);color:var(--white);text-align:center;font-style:italic;font-weight:700;font-size:11.5px;padding:2px 0;margin:2px 4px 10px}
.note{text-align:center;font-style:italic;font-weight:700;font-size:6.3px;line-height:1.3;margin-bottom:10px}
.photo{border-radius:6px}
.list-row{display:flex;align-items:baseline;font-size:7.2px;line-height:1.62}
.list-row .dots{flex:1;border-bottom:1px dotted var(--ink);margin:0 1px;transform:translateY(-2px)}
/* cover */
.hours{border:2px solid var(--green);margin:15px 10px 0;padding:8px 4px 10px;text-align:center;font-style:italic}
.hours h2{font-size:14px;font-weight:800;margin-bottom:10px}
.hours p{font-size:10.5px;line-height:1.4}
.call{text-align:center;font-style:italic;font-size:14px;line-height:1.4;margin-top:28px}
.site-small{text-align:center;font-style:italic;font-weight:600;font-size:9.5px;margin-top:18px}
.brand{display:flex;align-items:center;justify-content:center;gap:6px;font-weight:700;font-size:20px;color:var(--ink)}
.brand .mark{width:10px;height:10px;background:var(--green)}
.tagline{text-align:center;font-size:4.6px;letter-spacing:1px;margin-top:2px}
.badge{width:96px;height:96px;border-radius:50%;background:var(--green);margin:40px auto 0}
.cooked{text-align:center;font-style:italic;font-size:9.5px;position:absolute;left:0;right:0;bottom:55px}
.web-band{position:absolute;left:0;right:0;bottom:24px;background:var(--green);text-align:center;font-style:italic;font-weight:700;font-size:12px;padding:3px 0}
.key{border:1px solid var(--green);font-size:6.8px;line-height:1.35;padding:3px 6px;margin:4px 18px 14px}
.allergens{background:var(--green);margin:18px 6px 0;padding:5px 8px 8px;font-style:italic}
.allergens h3{text-align:center;font-size:9px;font-weight:700;margin-bottom:10px}
.allergens .cols{display:flex;justify-content:space-between;font-size:7.3px;line-height:1.35}
</style>
</head>
<body>

<div class="side-label" style="left:16px;top:136px">outside</div>
<div class="side-label" style="left:1050px;top:136px">inside</div>
<div class="side-label" style="left:26px;top:852px">inside</div>
<div class="side-label" style="left:1051px;top:852px">outside</div>

<!-- Outside: cover -->
<section class="sheet" style="left:145px;top:38px;width:394px;height:560px">
  <div class="panel white" style="padding:0">
    <div class="hours">
      <h2>OPENING HOURS</h2>
      <p>Sun - Thurs 5PM to 10.00PM<br>Fri - Sat 5.00PM-10.30PM</p>
      <p style="margin-top:12px">Deliveries From 5.30PM</p>
    </div>
    <div class="call">Call Now<br>015550142<br>015550178</div>
    <div class="site-small">www.saffronlane.ie</div>
    <div role="img" aria-label="Photo of spices in wooden bowls with star anise and cinnamon on a rustic table" style="position:absolute;left:0;right:0;bottom:14px;height:260px;background:linear-gradient(to bottom,rgba(255,255,255,0) 0%,#e8ddd0 25%,#b98a5e 60%,#6d4a2e 100%)"></div>
  </div>
  <div class="panel white" style="padding:0">
    <div role="img" aria-label="Photo of a vegetable curry in a steel thali with fresh chillies and tomatoes" style="height:230px;background:linear-gradient(to bottom,#5a4636 0%,#b76a2f 35%,#d9a05a 65%,#ffffff 100%)"></div>
    <div class="brand" style="margin-top:12px"><span class="mark"></span>Saffron Lane</div>
    <div class="tagline">AUTHENTIC INDIAN FOOD AT HOME</div>
    <div class="badge" role="img" aria-label="Natural food badge"></div>
    <div class="cooked">All our meals are cooked to order.</div>
    <div class="web-band">www.saffronlane.ie</div>
  </div>
</section>

<!-- Inside: top -->
<section class="sheet" style="left:632px;top:44px;width:396px;height:556px">
  <div class="panel green">
    <div class="head-box" style="margin-top:2px">Meal Deals only €8.50</div>
    <div class="note">(Low Fat Dishes)<br>Choose with Rice or Plain Naan</div>
    <div class="item"><div class="name">Chicken Dupiaza</div><div class="desc">Chicken cooked with ginger and chunks of onions and finished with onion seeds.........8.50</div></div>
    <div class="item"><div class="name">Chicken Rogan josh</div><div class="desc">A red chicken curry prepared with fresh herb &amp; spices, a delicacy from Kashmir..........8.50</div></div>
    <div class="item"><div class="name">Chicken Bhuna</div><div class="desc">Tomatoes and onion sauce cooked with black peppers &amp; spring onions.      8.50</div></div>
    <div class="item"><div class="name">Tarkari Makhani &nbsp;3,5</div><div class="desc">Mixed seasonal vegetables in a smooth tikka masala sauce.....8.50</div></div>
    <div class="item"><div class="name">Set Meal 1<span class="dots"></span>€16.00</div><ul><li>- Onion bhajia</li><li>- Chicken Tikka Masala</li><li>- Pilau rice</li><li>- Naan</li><li>- Poppadoms</li></ul></div>
    <div class="item"><div class="name">Set Meal For 2<span class="dots"></span>€27.00</div><ul><li>- Onion bhajia</li><li>- Chicken tikka</li><li>- Chicken Tikka Masala</li><li>- Lamb Roganjosh</li><li>- 2xPilau rice</li><li>- 1xNaan</li><li>- Poppadom</li></ul></div>
    <div class="item"><div class="name">Set Meal for 3/4<span class="dots"></span>€43.00</div><ul><li>- Onion bhajia</li><li>- Vegetable samosa</li><li>- Chicken tikka</li><li>- Chicken Tikka Masala</li><li>- Lamb Roganjosh</li><li>- Sambhar Veg Curry</li><li>- 2 x Pilau Rice</li><li>- 2 x Naan</li><li>- Poppadom</li></ul></div>
    <div class="photo" role="img" aria-label="Photo of golden onion bhajis on a plate with garlic and bread" style="margin-top:auto;height:105px;background:linear-gradient(135deg,#7a6a55 0%,#d7a14a 45%,#e9c27a 70%,#f3efe6 100%)"></div>
  </div>
  <div class="panel white">
    <div class="head-bar" style="margin-top:0">Healthy &nbsp;Side orders</div>
    <div class="item"><div class="name">Sautéed Broccoli &nbsp;&nbsp;(v)<span class="dots"></span>€5.00</div><div class="desc">Broccoli, green beans and spinach leaves sautéed with roasted cumin and fresh garlic.</div></div>
    <div class="item"><div class="name">Chana Saag -3 &nbsp;&nbsp;(y) (v)<span class="dots"></span>€5.00</div><div class="desc">Chickpeas cooked with chopped spinach, onion, and cumin and finished with cream.</div></div>
    <div class="item"><div class="name">Chana Masala &nbsp;&nbsp;(v)<span class="dots"></span>€5.00</div><div class="desc">Chickpeas simmered with tomato, caramelised onion, black pepper and fresh coriander.</div></div>
    <div class="item"><div class="name">Aloo Saag -3 &nbsp;&nbsp;(y) (v)<span class="dots"></span>€5.00</div><div class="desc">Crispy Potato with spinach, caramelised onion, garam masala and a dash of cream.</div></div>
    <div class="item"><div class="name">Aloo Ghobhi &nbsp;&nbsp;(v)<span class="dots"></span>€5.00</div><div class="desc">Crispy Potatoes cubes &amp; Cauliflower cooked with roasted cumin with tomato and onion gravy.</div></div>
    <div class="item"><div class="name">Tarka Daal &nbsp;4 &nbsp;&nbsp;(y) (v)<span class="dots"></span>€5.00</div><div class="desc">Home style soaked yellow chana cooked with cumin &amp; garam masala.</div></div>
    <div class="item"><div class="name">Tangy Aloo &nbsp;&nbsp;(v)<span class="dots"></span>€5.00</div><div class="desc">Crispy Potatoes cubes cooked with roasted cumin and touch of our tangy sauce</div></div>
    <div class="key">Y: Can be cooked without allergen<br>H: Healthy Option<br>V: Suitable for Vegans</div>
    <div class="head-bar" style="font-size:13px">Starters</div>
    <div class="item"><div class="name">Onion Bhajia<span class="dots"></span>€4.50</div><div class="desc">Spinach &amp; onions fritters flavored with mild spices</div></div>
    <div class="item"><div class="name">Vegetable Samosa &nbsp;2<span class="dots"></span>€4.50</div><div class="desc">Crispy Pastry stuffed with potatoes, chick peas, Green peas mixed with desi spices until golden.</div></div>
    <div class="item"><div class="name">Palak Tikki<span class="dots"></span>€4.50</div><div class="desc">Cakes of fresh spinach and chana dal</div></div>
    <div class="item"><div class="name">Veg Pakora<span class="dots"></span>€5.00</div><div class="desc">Cauliflower, potato and broccoli, golden fried with Gram flour batter.</div></div>
    <div class="item"><div class="name">Keema Singhara &nbsp;2<span class="dots"></span>€5.00</div><div class="desc">Spicy seasoned mince lamb in light pastry</div></div>
  </div>
</section>

<!-- Inside: bottom -->
<section class="sheet" style="left:141px;top:608px;width:400px;height:562px">
  <div class="panel green" style="padding-top:40px">
    <div class="item"><div class="name">Chicken Tikka &nbsp;3<span class="dots"></span>€5.00</div><div class="desc">Tender chicken marinated overnight with yoghurt, spices charred in tandoor</div></div>
    <div class="item"><div class="name">Seekh Kebab<span class="dots"></span>€5.50</div><div class="desc">Skewered hand pounder lamb glazed in tandoor with green chilli &amp; black cardamom.</div></div>
    <div class="item"><div class="name">Chicken Pakora<span class="dots"></span>€5.00</div><div class="desc">Boneless pieces of chicken coated in gram flour batter, with spices.</div></div>
    <div class="item"><div class="name">Chicken Wings &nbsp;2,1<span class="dots"></span>€5.00</div></div>
    <div class="item"><div class="name">Tandoori Mix Meat Platter &nbsp;3<span class="dots"></span>€9.50</div><div class="desc">Our special tandoori assortment of tandoori chicken on bone, seekh kebab and chicken tikka.</div></div>
    <div class="item"><div class="name">Mix Veg platter 2</div><div class="desc">Veg Samosa, Onion Bhaji,</div><div class="name" style="font-style:normal;font-weight:400;font-size:5.8px">Veg Pakora<span class="dots"></span>€6.50</div></div>
    <div class="item"><div class="name">Doner Kebab &nbsp;2,3,6<span class="dots"></span>€8.00</div><div class="desc">Stripes of minced chicken &amp; beef served with garlic mayo, chilli sauce &amp; mixed salad &amp; wrapped in naan.</div></div>
    <div class="item"><div class="name">Chicken Tikka Kebab &nbsp;2,3,6<span class="dots"></span>€8.00</div><div class="desc">Chicken breast marinated in spices, barbecued served with garlic mayo, chilli sauce &amp; mixed salad &amp; wrapped in naan</div></div>
    <div class="item"><div class="name">Mix Kebab &nbsp;2,3,6<span class="dots"></span>€8.00</div><div class="desc">Pieces of chicken tikka &amp; donner meat with garlic mayo, sweet chilli &amp; salad wrapped in naan bread</div></div>
    <div class="item"><div class="name">Garlic Chips<span class="dots"></span>€4.00</div></div>
    <div class="head-box" style="margin-top:8px">Chef Arora's Special Curries</div>
    <div class="item"><div class="name">Butter Murgh &nbsp;3,5<span class="dots"></span>€10.50</div><div class="desc">Chicken cooked in tandoor mixed with rich Tomato creamy cashew sauce, splash of cream with hint of honey &amp; dry fenugreek.</div></div>
    <div class="item"><div class="name">Laal Maas<span class="dots"></span>€11.50</div><div class="desc">Traditional rajasthani lamb cooked with garlic and ginger, degi chilli powder, tomatoes finished with star aniseed and clove powder.</div></div>
    <div class="item"><div class="name">Shahi Veg Kofta &nbsp;3'5<span class="dots"></span>€10.00</div><div class="desc">Handmade veg and panner dumplings simmered in tomato sauce, musky fenugreek sauce finished with touch of honey and cream.</div></div>
    <div class="item"><div class="name">Kerala Prawn &nbsp;14<span class="dots"></span>€12.00</div><div class="desc">Delicacy of kerala spices, tomato and red onion gravy finished with touch of fresh coconut milk.</div></div>
  </div>
  <div class="panel white" style="padding-top:28px">
    <div class="head-bar">Chicken Dishes</div>
    <div class="item"><div class="name">Punjabi Saag &nbsp;3 (y)<span class="dots"></span>€9.95</div><div class="desc">Chicken cooked with spinach, ginger, garlic, fresh cream &amp; temperd with Punjabi tarka.</div></div>
    <div class="item"><div class="name">Royale Korma &nbsp;3, 5<span class="dots"></span>€8.95</div><div class="desc">Breast of chicken cooked in a rich creamy sauce with saffron &amp; coconut, probably most popular among Irish.</div></div>
    <div class="item"><div class="name">Saffron Lane Chicken Curry &nbsp;3,4,5<span class="dots"></span>€8.95</div><div class="desc">Traditional curry cooked with coconut, mustard seed, cashews and curry leaves.</div></div>
    <div class="item"><div class="name">Chicken Karahi<span class="dots"></span>€8.95</div><div class="desc">Boneless chicken Prepared in Deg with peppers, onion, tomatoes and Indian whole spices.</div></div>
    <div class="item"><div class="name">Chicken Tikka Masala &nbsp;3<span class="dots"></span>€8.95</div><div class="desc">Chicken roasted in clayoven and simmered in smooth creamy tomato sauce with palm crushed fenugreek leaves and jiggery.</div></div>
    <div class="item"><div class="name">South Indian Garlic Chilli<span class="dots"></span>€8.95</div><div class="desc">Chicken cooked in south Indian style and loaded with garlic, ground spices, fresh herbs.</div></div>
    <div class="item"><div class="name">Chicken Dohiwala &nbsp;3<span class="dots"></span>€8.95</div><div class="desc">Amazingly spicy chicken curry cooked with yogurt, green chillies, ginger and herbs.</div></div>
    <div class="item"><div class="name">Murgh Biryani &nbsp;3,5 (y)<span class="dots"></span>€9.95</div><div class="desc">Perfumed basmati rice with chicken cubes, nuts, golden onions and biryani spices, served with sauce.</div></div>
    <div class="head-bar" style="margin-top:6px">Lamb Dishes</div>
    <div class="item"><div class="name">Lamb Madras<span class="dots"></span>€10.95</div><div class="desc">The popular dish of madras cooked with plum tomato, degi chilli, coconut and finished with hint of lemon juice.</div></div>
    <div class="item"><div class="name">Palak Gosht &nbsp;3 (y)<span class="dots"></span>€10.95</div><div class="desc">Pan-fried lamb pieces cooked with spinach, fresh herbs, ginger and touch of cream.</div></div>
    <div class="item"><div class="name">Lamb Roganjosh<span class="dots"></span>€10.95</div><div class="desc">Slow cooked tender lamb in kashmiri style with fresh herbs and Himalayan spices.</div></div>
    <div class="item"><div class="name">Lamb Kohlapuri &nbsp;3,4,5<span class="dots"></span>€10.95</div><div class="desc">lamb dish from South Coast of India Flavoured with yoghurt, nuts and coconut.</div></div>
  </div>
</section>

<!-- Outside: back -->
<section class="sheet" style="left:629px;top:610px;width:400px;height:561px">
  <div class="panel green" style="padding-top:28px">
    <div class="item"><div class="name">Lamb Jalferzi &nbsp;3,5<span class="dots"></span>€10.95</div><div class="desc">Lamb, tossed with cubes of onions, peppers flavored with crushed coriander seeds and dry fenugreek with hint of cream.</div></div>
    <div class="item"><div class="name">Gosht Biryani &nbsp;3,5 (y)<span class="dots"></span>€11.00</div><div class="desc">Aged rice cooked with tender land brown onions, home made masala and accompanied with curry sauce.</div></div>
    <div class="head-box">Prawn Dishes</div>
    <div class="item"><div class="name">Prawn Masala &nbsp;3<span class="dots"></span>€11.95</div><div class="desc">Prawns in a smooth creamy sauce flavoured with kasoori methi &amp; tandoori spices.</div></div>
    <div class="item"><div class="name">Prawn Karahi<span class="dots"></span>€11.95</div><div class="desc">Prawns cooked with peppers, spring onion, Caramelised onion, tomatoes &amp; whole spices</div></div>
    <div class="item"><div class="name">Goan Prawn Curry &nbsp;3,4,5<span class="dots"></span>€11.95</div><div class="desc">Fisherman's favourite prawn curry aromatic with coconut, mustard, nuts, curryleaves and spices fron goa's costal area.</div></div>
    <div class="item"><div class="name">Prawn Bhuna &nbsp;LF<span class="dots"></span>€11.95</div><div class="desc">Prawns cooked in onions &amp; tomato with black pepper to bought together the kick of spices</div></div>
    <div class="item"><div class="name">Prawn Biryani &nbsp;3,6 (y)<span class="dots"></span>€11.95</div><div class="desc">Pan fried prawn cooked with egg, green peas &amp; onion served with curry sauce.</div></div>
    <div class="head-box">Vegetarian Dishes</div>
    <div class="item"><div class="name">Shahi Paneer &nbsp;3, 5<span class="dots"></span>€8.95</div><div class="desc">Indian cheese in semi-dry sauce.</div></div>
    <div class="item"><div class="name">Subz Maloni Mild<span class="dots"></span>€8.95</div><div class="desc">Stir fried vegetables with ground spices.</div></div>
    <div class="item"><div class="name">Dum Wale Aloo &nbsp;3<span class="dots"></span>€8.95</div><div class="desc">Potatoes cooked with ginger, garlic, onions, yoghurt &amp; curry leave with cumin Flavored.</div></div>
    <div class="item"><div class="name">Karahi Paneer &nbsp;3<span class="dots"></span>€8.95</div><div class="desc">Colorful curry is prepared using homemade Indian cheese (paneer)</div></div>
    <div class="item"><div class="name">Saag Paneer &nbsp;3 (y)<span class="dots"></span>€8.95</div><div class="desc">Pan fried cottage cheese &amp; spinach with kasoori methi &amp;fresh coriander</div></div>
  </div>
  <div class="panel white" style="padding:28px 14px 0">
    <div class="head-bar" style="margin:0 0 4px">Nan Bread &amp; Side Orders</div>
    <div class="note" style="font-size:7px;margin-bottom:10px">All naan bread contains 2,3,6</div>
    <div class="list-row">Naan<span class="dots"></span>€2.20</div>
    <div class="list-row">Garlic Naan<span class="dots"></span>€2.50</div>
    <div class="list-row">Garlic Chilli Naan<span class="dots"></span>€3.00</div>
    <div class="list-row">Peshwari Naan &nbsp;5<span class="dots"></span>€3.00</div>
    <div class="list-row">Keema Naan<span class="dots"></span>€3.00</div>
    <div class="list-row">Coriander Naan<span class="dots"></span>€2.50</div>
    <div class="list-row">Chilli Cheese Naan 3<span class="dots"></span>€3.00</div>
    <div class="list-row">G.O.C.<span class="dots"></span>€3.00</div>
    <div class="list-row">Boiled Basmati<span class="dots"></span>€2.00</div>
    <div class="list-row">Pilau Rice<span class="dots"></span>€2.00</div>
    <div class="list-row">Lemon Rice 4<span class="dots"></span>€3.00</div>
    <div class="list-row">Poppodum(2)<span class="dots"></span>€2.50</div>
    <div class="list-row">Riata 3<span class="dots"></span>€2.50</div>
    <div class="allergens">
      <h3>Allergens</h3>
      <div class="cols">
        <div>Eggs<br>Nuts<br>Mustard<br>Crustaceans<br>Soya<br>Fish<br>Gluten</div>
        <div>Milk / Yoghurt<br>Sesame Seeds<br>Celery<br>Lupin<br>Peanuts<br>Molluscs<br>Sulpher dioxide</div>
      </div>
    </div>
    <div role="img" aria-label="Photo of dried red chillies and coriander seeds on a weathered wooden board" style="position:absolute;left:0;right:0;bottom:0;height:215px;background:linear-gradient(to bottom,rgba(255,255,255,0) 0%,#c9b8a2 25%,#7b4a33 55%,#8a1f1a 78%,#3e5a4c 100%)"></div>
  </div>
</section>

</body>
</html>
```